Fernvale Business Card Design

We are looking for a fresh business card design for our new logo. We would like a business card that is unique but friendly. We are in the window coverings business offering blinds, shutters and shades for homes.

Target Market(s)

Targeting the end-consumer

Industry/Entity Type

Business

Requirements
Must have
• Must have a dedicates space for a photo of our sales person. Must contain our new logo (attached).

```html
<!DOCTYPE html>
<html lang="en">
<head>
<meta charset="utf-8">
<title>Fernvale Business Card</title>
<link rel="stylesheet" href="https://fonts.googleapis.com/css2?family=Alegreya:wght@500&family=Open+Sans:wght@600&display=swap">
<style>
  :root {
    --backdrop: #626262;
    --foliage-dark: #173434;
    --foliage-mid: #2c4a44;
    --foliage-light: #4a6552;
    --frame: #ffffff;
    --panel: rgba(236, 240, 239, 0.93);
    --ink: #1e2c2c;
    --name-grey: #5a5a5a;
    --divider: #1b3535;
    --accent: #6cbf45;
  }
  * { box-sizing: border-box; margin: 0; padding: 0; }
  html, body { width: 958px; height: 1200px; overflow: hidden; }
  body { background: var(--backdrop); position: relative; font-family: "Open Sans", sans-serif; }

  .card { position: absolute; left: 81px; width: 811px; height: 486px; overflow: hidden; }
  .card--front { top: 88px; }
  .card--back { top: 638px; }

  .foliage-photo {
    position: absolute; inset: 0;
    background:
      radial-gradient(ellipse at 70% 30%, rgba(90,120,95,0.55), transparent 60%),
      radial-gradient(ellipse at 20% 80%, rgba(70,100,80,0.45), transparent 55%),
      linear-gradient(135deg, var(--foliage-mid), var(--foliage-dark) 55%, var(--foliage-light));
  }

  .frame { position: absolute; border: 5px solid var(--frame); }
  .frame--outer { left: 82px; top: 52px; width: 688px; height: 360px; }
  .frame--inner { left: 54px; top: 84px; width: 685px; height: 357px; }

  .brand { position: absolute; display: flex; flex-direction: column; align-items: center; font-family: "Alegreya", serif; font-weight: 500; }
  .brand__square { border: 4px solid currentColor; border-radius: 6px; }
  .brand--front { left: 0; width: 812px; top: 130px; color: #fff; }
  .brand--front .brand__square { width: 60px; height: 60px; margin-bottom: 34px; }
  .brand--front .brand__name { font-size: 62px; line-height: 1; }

  .panel { position: absolute; left: 52px; top: 46px; width: 718px; height: 392px; background: var(--panel); }

  .brand--back { left: 0; width: 380px; top: 172px; color: var(--name-grey); }
  .brand--back .brand__square { width: 46px; height: 46px; border-width: 3px; margin-bottom: 24px; }
  .brand--back .brand__name { font-size: 45px; line-height: 1; }

  .divider { position: absolute; left: 355px; top: 71px; width: 3px; height: 243px; background: var(--divider); }

  .photo-slot { position: absolute; left: 544px; top: 47px; width: 96px; height: 112px; border: 1.5px solid var(--ink); }

  .contacts { position: absolute; left: 409px; top: 188px; list-style: none; color: var(--ink); font-size: 14px; line-height: 21px; }
  .contacts li { display: flex; align-items: flex-start; gap: 11px; margin-bottom: 18px; }
  .contacts li:nth-child(3) { margin-bottom: 12px; }
  .contacts svg { width: 22px; height: 21px; flex: none; fill: var(--accent); }
</style>
</head>
<body>
  <section class="card card--front">
    <div class="foliage-photo" role="img" aria-label="Dark green leaves with water droplets"></div>
    <div class="frame frame--outer"></div>
    <div class="frame frame--inner"></div>
    <div class="brand brand--front">
      <span class="brand__square"></span>
      <span class="brand__name">Fernvale</span>
    </div>
  </section>

  <section class="card card--back">
    <div class="foliage-photo" role="img" aria-label="Dark green leaves with water droplets"></div>
    <div class="panel">
      <div class="brand brand--back">
        <span class="brand__square"></span>
        <span class="brand__name">Fernvale</span>
      </div>
      <div class="divider"></div>
      <div class="photo-slot" aria-label="Space for sales person photo"></div>
      <ul class="contacts">
        <li>
          <svg viewBox="0 0 22 21"><path d="M1 5h20v12H1z"/><path d="M1 5l10 7 10-7" fill="none" stroke="#fff" stroke-width="1.5"/></svg>
          <span>HELLO@FERNVALESHADES.COM</span>
        </li>
        <li>
          <svg viewBox="0 0 22 21"><path d="M5 2l4 1 1 4-2 2c1 3 3 5 6 6l2-2 4 1 1 4-2 2C10 20 2 12 3 4z"/></svg>
          <span>+1 555 0142 3380</span>
        </li>
        <li>
          <svg viewBox="0 0 22 21"><path d="M11 2l10 9h-3v8h-5v-5h-4v5H4v-8H1z"/></svg>
          <span>48 LINDEN GROVE AVENUE<br>MAPLE HEIGHTS, OR, USA</span>
        </li>
        <li>
          <svg viewBox="0 0 22 21"><circle cx="11" cy="10.5" r="9.5"/><path d="M6 6c3 0 3 3 5 3s1 3 3 4-1 4-3 5M14 3c-1 2 1 3 3 3" fill="none" stroke="#fff" stroke-width="1.5"/></svg>
          <span>WWW.FERNVALESHADES.COM</span>
        </li>
      </ul>
    </div>
  </section>
</body>
</html>
```